Medical Device Packaging Project 1 of 5

We are a medical device startup company needing packaging for a total of 5 device brands. This is posting 1 of 5 and the device name is "Vexomira"

Vexomira is an intraocular lens for use in cataract surgery. The target market is Chinese ophthalmologists. The box should be sophisticated and upmarket.

The company name is Tambrel Vision, I have included the logo in the uploaded files section. You should include the logo on the box.

I have uploaded a sample lens boxes from other companies that demonstrate the information needed to be contained on the box in terms of address, warnings, symbols, etc.

I have also uploaded the blank dieline of the boxes

You are welcome and encouraged to also submit to projects 2, 3, 4, and 5 as well. The same rules and expectations apply.

Industry/Entity Type

It Company

Requirements
Should not have
• Should not have any images of an eye or any bionic/futuristic feel to the design
• Note that the quindaret box is for text reference only. You may use the lens image but the futuristic/bionic look is NOT what we are going for with this brand. It should be traditional upmarket medical device artwork.

```html
<!DOCTYPE html>
<html lang="en">
<head>
<meta charset="utf-8">
<title>Vexomira – Intraocular Lens Box</title>
<link rel="stylesheet" href="https://fonts.googleapis.com/css2?family=Libre+Baskerville:ital,wght@0,400;1,400&display=swap">
<style>
  :root {
    --stage: #e6e7e8;
    --panel: #d3d6d8;
    --panel-light: #dfe2e4;
    --navy: #1d3447;
    --navy-deep: #172b3b;
    --strip: #e8eaeb;
    --ink-light: #eef1f3;
    --ink-navy: #1d3447;
    --lens-dark: #5d6a70;
    --lens-light: #b8c2c6;
  }
  * { margin: 0; padding: 0; box-sizing: border-box; }
  html, body { width: 1200px; height: 675px; overflow: hidden; background: var(--stage); }
  .canvas { position: relative; width: 1200px; height: 675px; }

  .top-face {
    position: absolute; left: 200px; top: 30px; width: 800px; height: 380px;
    background: var(--panel);
    overflow: hidden;
  }
  .backdrop-art {
    position: absolute; left: 180px; top: 0; width: 460px; height: 240px;
    background: radial-gradient(ellipse at 50% 40%, var(--panel-light) 0%, rgba(211,214,216,0) 70%);
  }
  .lens-art {
    position: absolute; left: 300px; top: 34px; width: 200px; height: 96px;
    border-radius: 48px;
    background: radial-gradient(circle at 50% 50%, var(--lens-dark) 0 22%, var(--lens-light) 23% 28%, rgba(140,152,158,0.35) 40%, rgba(211,214,216,0) 70%);
  }
  .name-band {
    position: absolute; left: 0; top: 168px; width: 380px; height: 64px;
    background: var(--navy);
    display: flex; align-items: center; padding-left: 60px;
  }
  .product-name {
    font-family: "Libre Baskerville", serif; font-style: italic;
    color: var(--ink-light); font-size: 40px; letter-spacing: 4px;
  }
  .type-strip {
    position: absolute; left: 380px; top: 232px; width: 420px; height: 40px;
    background: var(--strip);
    display: flex; align-items: center; padding-left: 24px;
  }
  .product-type {
    font-family: "Libre Baskerville", serif; color: var(--ink-navy);
    font-size: 17px; letter-spacing: 1px;
  }
  .brand {
    position: absolute; right: 50px; top: 150px;
    display: flex; align-items: center; gap: 12px;
  }
  .brand-dot { width: 26px; height: 26px; border-radius: 50%; background: var(--navy); }
  .brand-name {
    font-family: "Libre Baskerville", serif; color: var(--ink-navy);
    font-size: 22px; letter-spacing: 3px;
  }

  .front-face {
    position: absolute; left: 200px; top: 420px; width: 800px; height: 225px;
    background: var(--navy-deep);
    display: flex;
  }
  .front-spine {
    width: 80px; display: flex; align-items: center; justify-content: center;
  }
  .vertical-name {
    font-family: "Libre Baskerville", serif; font-style: italic;
    color: var(--ink-light); font-size: 20px; letter-spacing: 3px;
    writing-mode: vertical-rl;
  }
  .front-body {
    flex: 1; display: flex; align-items: center; justify-content: space-between;
    padding: 0 40px;
  }
  .front-note {
    font-family: "Libre Baskerville", serif; color: var(--ink-light);
    font-size: 11px; line-height: 1.8; max-width: 330px; opacity: 0.75;
  }
  .front-brand { display: flex; align-items: center; gap: 10px; }
  .front-brand .brand-dot { width: 18px; height: 18px; background: var(--ink-light); }
  .front-brand .brand-name { color: var(--ink-light); font-size: 13px; letter-spacing: 2px; }
  .front-end {
    width: 110px; background: var(--panel);
    display: flex; align-items: center; justify-content: center;
  }
  .front-end .vertical-name { color: var(--ink-navy); }
</style>
</head>
<body>
<main class="canvas">
  <section class="top-face">
    <div class="backdrop-art" role="img" aria-label="Faint background illustration in soft grey tones"></div>
    <div class="lens-art" role="img" aria-label="Intraocular lens with curved haptics"></div>
    <div class="name-band"><h1 class="product-name">Vexomira</h1></div>
    <div class="type-strip"><p class="product-type">INTRAOCULAR LENS</p></div>
    <div class="brand"><span class="brand-dot"></span><span class="brand-name">TAMBREL VISION</span></div>
  </section>

  <section class="front-face">
    <div class="front-spine"><span class="vertical-name">Vexomira</span></div>
    <div class="front-body">
      <p class="front-note">Sterile single use intraocular lens. Store dry at room temperature.</p>
      <div class="front-brand"><span class="brand-dot"></span><span class="brand-name">TAMBREL VISION</span></div>
    </div>
    <div class="front-end"><span class="vertical-name">Vexomira</span></div>
  </section>
</main>
</body>
</html>
```